Banner Ad Design Project

I need a banner design. The website is under construction at www.brightmarrow.example

Name: Bright Marrow
Tagline: Steady Sparks for crowded calendars

This is a leadership development and executive coaching site. The past site is live at www.quillstepnow.example. (so you can get a sense of the content)

The audience are (BUSY) executives, senior managers, leaders and top professionals, so the feel needs to be highly professional but also modern and fresh. I want to communicate energy but also solid and trust worthy and not too new agey. The audience are also people with strong social values who want to change things - so not too corporate (Ie suits!)

I would like the design to be floating on a white background, very clean and simple. I am attracted to reds or sunset (burn orange crimson colors.) But totally open to any color ideas.
I am giving an open brief for your ideas.
Here are the dimensions 960px wide, roughly 190px height.

Reason: The weekend might give more time to designers to get involved. Thanks Vina

Hi designers

You may not have seen the additions I gave to this brief.

The banner should not have leader out front photo's. Maybe less corporate than I initially thought. 
Not too corporate (no suits!) Please no chess pieces, jigsaw pieces, cartoon images, cliche leadership images. 
Am am trying for inspiration /inspiring whilst still being professional. Very simple and clean.
Please can the design be floating in a white background so that the web page is borderless - A bit like it is in http://palmoriskel.example/
Thank you

Target Market(s)

Senior managers, executives but people who also want to change the world!

Industry/Entity Type

Construction

Requirements
Should not have
• Should not have leader out front photo's.
Maybe less corporate than I initially thought.
Am am trying for inspiration /inspiring whilst still being professional.
Please no chess pieces, jigsaw pieces, cartoon images, cliche leadership images. Not too corporate (Ie suits!)

Thanks

```html
<!DOCTYPE html>
<html lang="en">
<head>
<meta charset="utf-8">
<title>Bright Marrow – Banner</title>
<link rel="stylesheet" href="https://fonts.googleapis.com/css2?family=Crimson+Text:wght@400&family=PT+Sans:wght@400&display=swap">
<style>
  :root {
    --navy-deep: #1a3582;
    --navy-mid: #24469e;
    --navy-light: #2f56b0;
    --watermark: rgba(140, 170, 230, 0.16);
    --title: #ffffff;
    --tagline: #f2a31b;
    --arrow: #d8202a;
    --photo-dark: #1b2a55;
    --photo-warm: #c99a7c;
    --photo-light: #e6c4aa;
  }
  html, body {
    margin: 0;
    padding: 0;
    width: 1200px;
    height: 238px;
    overflow: hidden;
    background: #ffffff;
  }
  .banner {
    position: relative;
    width: 1200px;
    height: 238px;
    overflow: hidden;
    background: linear-gradient(90deg, var(--navy-deep) 0%, var(--navy-mid) 45%, var(--navy-light) 100%);
  }
  .watermark {
    position: absolute;
    margin: 0;
    font-family: "PT Sans", sans-serif;
    font-weight: 400;
    color: var(--watermark);
    white-space: nowrap;
    line-height: 1;
    letter-spacing: -1px;
  }
  .watermark--top {
    left: 292px;
    top: -44px;
    font-size: 140px;
  }
  .watermark--bottom {
    left: -4px;
    top: 104px;
    font-size: 166px;
  }
  .title {
    position: absolute;
    left: 48px;
    top: 32px;
    margin: 0;
    font-family: "Crimson Text", serif;
    font-weight: 400;
    font-size: 52px;
    line-height: 1;
    color: var(--title);
  }
  .tagline {
    position: absolute;
    left: 48px;
    top: 111px;
    margin: 0;
    font-family: "PT Sans", sans-serif;
    font-size: 26px;
    line-height: 1;
    color: var(--tagline);
    display: flex;
    align-items: center;
    gap: 12px;
  }
  .tagline svg { display: block; }
  .photo {
    position: absolute;
    left: 815px;
    top: 0;
    width: 385px;
    height: 238px;
    background:
      radial-gradient(ellipse 60% 55% at 55% 55%, var(--photo-light) 0%, var(--photo-warm) 45%, rgba(201,154,124,0) 80%),
      linear-gradient(90deg, var(--photo-dark) 0%, #3a4670 40%, #6a6f88 100%);
  }
</style>
</head>
<body>
  <div class="banner">
    <p class="watermark watermark--top" aria-hidden="true">Inspiration</p>
    <p class="watermark watermark--bottom" aria-hidden="true">Leadership</p>
    <h1 class="title">Bright Marrow</h1>
    <p class="tagline">Steady Sparks for crowded calendars
      <svg width="12" height="20" viewBox="0 0 12 20" aria-hidden="true"><polygon points="0,0 12,10 0,20" fill="var(--arrow)"/></svg>
    </p>
    <div class="photo" role="img" aria-label="Photo of many hands stacked together in a team gesture"></div>
  </div>
</body>
</html>
```